Wedding Music Playlist Template

Hi, I'm a wedding musician and I'd like a 1 pager wedding music template created. It needs to be editable for future weddings.

At the top of the template:
Bride First Name & Groom First Name plus 's WEDDING
Date of Wedding:
Venue name:

(The form needs to be flexible where I can remove/interchange Prelude Ceremony / Ceremony / Canapes / Reception) as sometimes I will play music just for a Ceremony sometimes for both Ceremony/Canapes or sometimes just the reception only or all of the above.

Section 1: Prelude Ceremony (this could be up to 5 songs)

Section 2: Ceremony
Processional (this is sometimes 1 or 2 songs)
Signing of Papers (this is sometimes 1 or 2 songs)
Recessional (1 song)

Section 3: Canapes

Section 4: Reception

Within each section
Artist
Song

I'd also like the template to feature
logo (attached) and social media links
website URL tolvercade.com.au
instagram: tolvercademusic
facebook: tolvercadepianist
soundcloud: keyglow_nuptials

I see the form/template serving two purposes.
1) I'll send back to the bride when she books me for a wedding and she may socialise it.
2) Posting on instagram as I perform at each wedding and attract engaged brides looking for wedding pianist or even just ideas for wedding music.
Updates

Target Market(s)

Engaged Couples looking for wedding music or suggested music for wedding

Industry/Entity Type

Wedding

Requirements
Must have
• Please see project description.
Nice to have
• Background wedding image with text overlayed

```html
<!DOCTYPE html>
<html lang="en">
<head>
<meta charset="utf-8">
<title>Wedding Music Playlist</title>
<link href="https://fonts.googleapis.com/css2?family=Great+Vibes&family=Cormorant+Garamond:ital,wght@0,400;0,600;1,400&display=swap" rel="stylesheet">
<style>
  :root {
    --backdrop: #e9e9e9;
    --paper: #ffffff;
    --teal: #1a9c9c;
    --ink: #2a2a2a;
    --muted: #6a6a6a;
    --photo-light: #f1f1f3;
    --photo-mid: #d9dbe0;
    --photo-accent: #c9525a;
  }
  * { box-sizing: border-box; margin: 0; padding: 0; }
  html, body { width: 1200px; height: 1200px; overflow: hidden; background: var(--backdrop); }
  body { display: flex; align-items: center; justify-content: center; font-family: "Cormorant Garamond", serif; color: var(--ink); }

  .flyer { position: relative; width: 806px; height: 1140px; background: var(--paper); box-shadow: 0 4px 18px rgba(0,0,0,.12); overflow: hidden; }

  .hero { position: absolute; left: 0; top: 0; width: 100%; height: 530px; }
  .hero svg { display: block; width: 100%; height: 100%; }

  .brand { position: absolute; left: 56px; top: 52px; display: flex; align-items: center; gap: 12px; }
  .brand-dot { width: 38px; height: 38px; border-radius: 50%; background: var(--ink); }
  .brand-name { font-weight: 600; font-size: 21px; letter-spacing: 1px; line-height: 1; }
  .brand-tag { font-size: 13px; color: var(--muted); margin-top: 3px; }

  .names { position: absolute; top: 495px; width: 100%; text-align: center; font-family: "Great Vibes", cursive; color: var(--teal); font-size: 78px; line-height: 1; }
  .date-line { position: absolute; top: 585px; width: 100%; text-align: center; font-size: 19px; letter-spacing: .5px; }
  .date-line .script { font-family: "Great Vibes", cursive; color: var(--teal); font-size: 34px; margin-left: 8px; vertical-align: -4px; }
  .venue { position: absolute; top: 622px; width: 100%; text-align: center; font-size: 19px; letter-spacing: 1px; display: flex; justify-content: center; align-items: center; gap: 6px; }
  .venue svg { width: 13px; height: 17px; }

  .programme { position: absolute; top: 660px; width: 100%; text-align: center; font-size: 12.5px; line-height: 1.42; }
  .section-title { font-weight: 600; letter-spacing: 1px; margin-top: 7px; }
  .sub-title { color: var(--muted); font-style: italic; }
  .song { font-style: italic; color: var(--muted); }

  .contacts { position: absolute; bottom: 40px; left: 0; width: 100%; display: flex; justify-content: center; flex-wrap: wrap; gap: 8px 46px; padding: 0 90px; font-size: 13px; color: var(--muted); }
  .contact { display: flex; align-items: center; gap: 7px; }
  .contact-dot { width: 14px; height: 14px; border-radius: 50%; background: var(--teal); }
</style>
</head>
<body>
  <main class="flyer">
    <div class="hero" role="img" aria-label="Photograph of a couple's hands resting beside a red and white wedding bouquet">
      <svg viewBox="0 0 806 530" preserveAspectRatio="none">
        <defs>
          <linearGradient id="heroFill" x1="0" y1="0" x2="1" y2="1">
            <stop offset="0" stop-color="#fafafa"/>
            <stop offset=".45" stop-color="#e4e5ea"/>
            <stop offset=".6" stop-color="#d8b7b4"/>
            <stop offset="1" stop-color="#d2d4da"/>
          </linearGradient>
        </defs>
        <path d="M0 0 H806 V330 C640 380 470 440 0 430 Z" fill="url(#heroFill)"/>
      </svg>
    </div>

    <div class="brand">
      <span class="brand-dot"></span>
      <div>
        <div class="brand-name">TOLVERCADE</div>
        <div class="brand-tag">Wedding &amp; Event Pianist</div>
      </div>
    </div>

    <h1 class="names">Clara &amp; Julian's</h1>
    <p class="date-line">SAT August 26<sup>th</sup> 2017 <span class="script">Wedding</span></p>
    <p class="venue">
      <svg viewBox="0 0 12 16"><path d="M6 0a6 6 0 0 0-6 6c0 4.5 6 10 6 10s6-5.5 6-10a6 6 0 0 0-6-6zm0 8.5a2.5 2.5 0 1 1 0-5 2.5 2.5 0 0 1 0 5z" fill="var(--teal)"/></svg>
      FERNHOLLOW ESTATE
    </p>

    <section class="programme">
      <p class="section-title">SECTION 1: PRELUDE CEREMONY</p>
      <p class="song">1. Golden Hour – The Lanterns</p>
      <p class="song">2. Still Waters – Mara Vale</p>
      <p class="song">3. Paper Moon – Ivy Hart</p>
      <p class="song">4. Quiet Harbour – Sol Reed</p>
      <p class="song">5. First Light – Ana Bloom</p>

      <p class="section-title">SECTION 2: CEREMONY</p>
      <p class="sub-title">Processional</p>
      <p class="song">Slow Dance – Eli Grey</p>
      <p class="sub-title">Signing of Papers</p>
      <p class="song">Ever After – June Park / Little Things – Rowan</p>
      <p class="sub-title">Recessional</p>
      <p class="song">Sunlit Road – The Daybreaks</p>

      <p class="section-title">SECTION 3: CANAPES</p>
      <p class="song">Open Sky – Leo Finch · Blue Garden – Nia Rose</p>

      <p class="section-title">SECTION 4: RECEPTION</p>
      <p class="song">Together – Kai Stone</p>
    </section>

    <footer class="contacts">
      <span class="contact"><span class="contact-dot"></span>tolvercade.com.au</span>
      <span class="contact"><span class="contact-dot"></span>tolvercademusic</span>
      <span class="contact"><span class="contact-dot"></span>tolvercadepianist</span>
      <span class="contact"><span class="contact-dot"></span>keyglow_nuptials</span>
    </footer>
  </main>
</body>
</html>
```